Brava Set CEO and Partners Business Card

We need a fresh, fun, simple and clean business card design....we would like a template where we can add a name and title (as well as specific email addresses). We are open to different looks (full logo on one side and a small logo on the company info side, or our logo is in the background but faint on one side but full on the other, or something else cool :-) ). Our colors are in our logo: blue, black and white...however we are not opposed to the use of other colors if it works. We build sets, make props and a host of other things for the film and television industry...our card should reflect creativity, style and professionalism.

A white background would be preferred.

I would like to see an option with Facebook and Instagram icons.

Facebook- facebook.com/bravasetny
Instagram- brava_set

Our website is bravaset-example.com.

Brava Set, Inc.
418 Corvell Avenue, Unit 9
North Hollywood, California 91602
555.210.4873 | tel
555.210.6692 | fax
www.BravaSet-example.com

Sample Name and Title #1:

Peter Halvik
CEO / Co-Owner
555.210.4873 | tel
555.210.6692 | fax
peter@bravaset-example.com
www.BravaSet-example.com

Target Market(s)

Marketing Professionals, Production Designers, Interior Designers, Film Producers, Directors, Art Directors, Event Directors

Industry/Entity Type

Entertainment Industry

Contact Information for Business Card

Peter Halvik
CEO / Co-Owner
555.210.4873 | tel
555.210.6692 | fax
peter@bravaset-example.com
www.BravaSet-example.com

Font styles to use
Sans Serif

Colors
33a6d7
ffffff
1b1b1b

Requirements
Must have
• Logo, All Contact Info, White Background. Symmetry.
Nice to have
• Facebook and Instagram icons with addresses
• Facebook- facebook.com/bravasetny
• Instagram- brava_set

```html
<!DOCTYPE html>
<html lang="en">
<head>
<meta charset="utf-8">
<title>Brava Set Business Card</title>
<link href="https://fonts.googleapis.com/css2?family=Open+Sans:wght@400;600;800&display=swap" rel="stylesheet">
<style>
  :root {
    --brand-blue: #33a6d7;
    --ink: #1b1b1b;
    --paper: #ffffff;
    --stage: #e9eaec;
    --muted: #4a4a4a;
  }
  * { margin: 0; padding: 0; box-sizing: border-box; }
  html, body { width: 1200px; height: 900px; overflow: hidden; }
  body {
    background: var(--stage);
    font-family: "Open Sans", Arial, sans-serif;
    color: var(--ink);
    position: relative;
  }
  .card {
    position: absolute;
    top: 302px;
    width: 520px;
    height: 296px;
    box-shadow: 0 6px 18px rgba(0,0,0,0.12);
  }
  .card-front { left: 60px; background: var(--paper); }
  .card-back {
    left: 620px;
    background: var(--brand-blue);
    display: flex; align-items: center; justify-content: center;
  }
  .wordmark {
    font-weight: 800;
    letter-spacing: 1px;
    text-transform: uppercase;
    line-height: 1;
  }
  .card-back .wordmark { color: var(--paper); font-size: 56px; }
  .card-front .wordmark {
    position: absolute; left: 262px; top: 112px;
    color: var(--ink); font-size: 44px;
  }
  .contact-block { position: absolute; left: 30px; top: 32px; }
  .person-name { color: var(--brand-blue); font-weight: 600; font-size: 15px; }
  .person-title { font-size: 11px; color: var(--muted); margin-bottom: 10px; }
  .contact-list { list-style: none; font-size: 11px; color: var(--muted); }
  .contact-list li { display: flex; align-items: flex-start; gap: 7px; line-height: 16px; }
  .contact-list svg { flex: 0 0 10px; margin-top: 3px; }
  .address-item { margin-top: 4px; }
  .social-block {
    position: absolute; right: 30px; bottom: 28px;
    list-style: none; font-size: 11.5px; color: var(--muted); text-align: right;
  }
  .social-block li { display: flex; justify-content: flex-end; align-items: center; gap: 8px; line-height: 19px; }
  .social-square { width: 11px; height: 11px; background: var(--brand-blue); border-radius: 2px; }
</style>
</head>
<body>
  <section class="card card-front" aria-label="Business card front">
    <div class="contact-block">
      <p class="person-name">Peter Halvik</p>
      <p class="person-title">CEO / Co-Owner</p>
      <ul class="contact-list">
        <li><svg width="10" height="10" viewBox="0 0 10 10"><path d="M2 0h2l1 3-1.5 1a6 6 0 0 0 2.5 2.5L7 5l3 1v2a2 2 0 0 1-2 2A8 8 0 0 1 0 2a2 2 0 0 1 2-2z" fill="#33a6d7"/></svg>555.210.4873</li>
        <li><svg width="10" height="10" viewBox="0 0 10 10"><rect x="1" y="3" width="8" height="6" rx="1" fill="#33a6d7"/><rect x="3" y="0" width="4" height="3" fill="#33a6d7"/></svg>555.210.6692</li>
        <li><svg width="10" height="10" viewBox="0 0 10 10"><rect x="0" y="2" width="10" height="7" rx="1" fill="#33a6d7"/><path d="M0 3l5 3 5-3" stroke="#fff" fill="none"/></svg>peter@bravaset-example.com</li>
        <li><svg width="10" height="10" viewBox="0 0 10 10"><circle cx="5" cy="5" r="4" stroke="#33a6d7" fill="none" stroke-width="1.3"/><path d="M1 5h8M5 1v8" stroke="#33a6d7"/></svg>www.BravaSet-example.com</li>
        <li class="address-item"><svg width="10" height="10" viewBox="0 0 10 10"><path d="M5 0a3.5 3.5 0 0 1 3.5 3.5C8.5 6 5 10 5 10S1.5 6 1.5 3.5A3.5 3.5 0 0 1 5 0z" fill="#33a6d7"/><circle cx="5" cy="3.5" r="1.2" fill="#fff"/></svg><span>418 Corvell Avenue, Unit 9<br>North Hollywood, California 91602</span></li>
      </ul>
    </div>
    <p class="wordmark">Brava Set</p>
    <ul class="social-block">
      <li>facebook.com/bravasetny <span class="social-square"></span></li>
      <li>instagram.com/brava_set <span class="social-square"></span></li>
    </ul>
  </section>

  <section class="card card-back" aria-label="Business card back">
    <p class="wordmark">Brava Set</p>
  </section>
</body>
</html>
```